In Home Personal IT Consultant (Nerd) Website and Logo QTgeek.net

Website and logo design for in home personal "nerd". Consulting services provided: Home Automation, Home Theater, Network and Wi-Fi installation, Computer Repair, and Virus Removal. Need simple site to promote QTgeek.net based in Santa Fe, New Mexico. You may choose to incorporate the Zia symbol from the New Mexico flag into the design, not mandatory. I am also a big fan of the movie Return of the Tinkers.
I have over 10 years of experience in the hospitality industry working with multi million dollar hotels and will apply that same level of service to the home. TechVara B+ and Shieldwise+ Certified. Available by appointment, primarily Evenings and Weekends. Consulting rate will be $70/hr.
Industry/Entity Type
Consulting
Number of Pages Required
1 page
Look and feel
Each slider illustrates characteristics of the customer's brand and the style your logo design should communicate.

```html
<!DOCTYPE html>
<html lang="en">
<head>
<meta charset="UTF-8">
<title>QTgeek.net — In Home Personal IT Consultant</title>
<link href="https://fonts.googleapis.com/css2?family=Montserrat:wght@600;700;800&family=Open+Sans:wght@400;600;700&display=swap" rel="stylesheet">
<style>
  :root {
    --page-bg: #e4e4e4;
    --accent: #f05442;
    --accent-ghost: rgba(255,255,255,0.14);
    --dark: #333333;
    --ink: #3a3a3a;
    --white: #ffffff;
    --hero-light: #f6f6f6;
    --hero-mid: #d9d9d9;
  }
  * { margin: 0; padding: 0; box-sizing: border-box; }
  html, body { width: 1200px; height: 1000px; overflow: hidden; }
  body {
    position: relative;
    background: var(--page-bg);
    font-family: "Open Sans", Arial, sans-serif;
  }
  .site { position: absolute; left: 189px; top: 172px; width: 823px; height: 828px; box-shadow: 0 0 18px rgba(0,0,0,0.12); }

  .hero {
    position: absolute; left: 0; top: 0; width: 823px; height: 360px;
    background: linear-gradient(180deg, var(--hero-light) 0%, #ececec 70%, var(--hero-mid) 100%);
  }
  .about { position: absolute; left: 0; top: 360px; width: 823px; height: 318px; background: var(--dark); }
  .skills {
    position: absolute; left: 0; top: 678px; width: 823px; height: 150px;
    background: linear-gradient(180deg, #e9e9e9, #dcdcdc);
  }

  .brand-column {
    position: absolute; left: 256px; top: 86px; width: 205px; height: 914px;
    background: var(--accent); overflow: hidden;
  }
  .brand-name {
    position: absolute; left: 0; top: 18px; width: 205px; text-align: center;
    font-family: "Montserrat", Arial, sans-serif; font-weight: 800; font-size: 45px;
    color: var(--white); letter-spacing: -1px; line-height: 1;
  }
  .brand-tagline {
    position: absolute; left: 0; top: 64px; width: 205px; text-align: center;
    font-family: "Montserrat", Arial, sans-serif; font-weight: 700; font-size: 11.5px;
    color: var(--white);
  }
  .ghost-word {
    position: absolute; font-family: "Montserrat", Arial, sans-serif; font-weight: 800;
    color: transparent; -webkit-text-stroke: 3px var(--accent-ghost);
    font-size: 78px; line-height: 1; white-space: nowrap;
  }
  .section-title {
    position: absolute; left: 0; width: 205px; text-align: center;
    font-family: "Montserrat", Arial, sans-serif; font-weight: 700; font-size: 28px;
    color: var(--white); text-shadow: 0 3px 6px rgba(0,0,0,0.35);
  }

  .nav { position: absolute; right: 248px; top: 89px; display: flex; align-items: center; gap: 10px; }
  .nav a {
    font-family: "Open Sans", Arial, sans-serif; font-weight: 700; font-size: 20px;
    color: var(--ink); text-decoration: none;
  }
  .nav .dot { width: 8px; height: 8px; background: var(--accent); }
  .menu-toggle { position: absolute; left: 970px; top: 86px; width: 42px; height: 34px; }

  .hero-products {
    position: absolute; left: 220px; top: 205px; width: 735px; height: 300px;
    background: radial-gradient(ellipse at 50% 45%, #8a7a62 0%, #5a5a5e 40%, rgba(40,40,44,0.15) 75%, rgba(255,255,255,0) 100%);
    border-radius: 8px;
  }

  .about-body { position: absolute; left: 498px; top: 560px; width: 446px; color: var(--white); font-size: 9.6px; line-height: 11.3px; }
  .about-body p strong { font-weight: 700; }
  .callout { position: relative; margin: 12px 0 0 17px; padding-left: 17px; }
  .callout::before { content: ""; position: absolute; left: 0; top: 0; width: 7px; height: 100%; background: var(--accent); }
  .callout h3 { font-size: 9.6px; font-weight: 700; margin-bottom: 11px; }

  .service-photo {
    position: absolute; left: 498px; top: 893px; width: 205px; height: 107px;
    background: linear-gradient(135deg, #8c8c8c, #3c3c3c 60%, #9a9a9a);
  }
  .service-card { position: absolute; left: 703px; top: 893px; width: 240px; height: 107px; background: var(--white); }
  .service-card h2 {
    position: absolute; left: 15px; top: 10px;
    font-family: "Montserrat", Arial, sans-serif; font-weight: 600; font-size: 23px; color: #444;
  }
  .service-card p {
    position: absolute; left: 43px; top: 55px; width: 185px; padding-left: 0;
    font-size: 9.6px; line-height: 11.3px; color: #555;
  }
  .service-card .bar { position: absolute; left: 26px; top: 52px; width: 7px; height: 60px; background: var(--accent); }
</style>
</head>
<body>
  <main class="site">
    <section class="hero"></section>
    <section class="about"></section>
    <section class="skills" role="img" aria-label="Faint grey circuit-board line pattern background"></section>
  </main>

  <aside class="brand-column">
    <div class="brand-name">QTgeek</div>
    <div class="brand-tagline">In Home Personal IT Consultant</div>
    <span class="ghost-word" style="left:-12px; top:500px;">ABOUT</span>
    <span class="ghost-word" style="left:26px; top:612px;">ABOUT</span>
    <h2 class="section-title" style="top:520px;">ABOUT</h2>
    <span class="ghost-word" style="left:-40px; top:815px;">SKILLS</span>
    <h2 class="section-title" style="top:838px;">SKILLS</h2>
  </aside>

  <nav class="nav">
    <a href="#">Home</a><span class="dot"></span>
    <a href="#">About</a><span class="dot"></span>
    <a href="#">Skills</a><span class="dot"></span>
    <a href="#">Contact</a>
  </nav>
  <svg class="menu-toggle" viewBox="0 0 42 34" aria-label="Menu">
    <rect x="0" y="0" width="42" height="7" fill="#f05442"/>
    <rect x="0" y="13" width="42" height="7" fill="#f05442"/>
    <rect x="0" y="26" width="42" height="8" fill="#f05442"/>
  </svg>

  <div class="hero-products" role="img" aria-label="Home theater subwoofer and speakers, a desktop monitor showing a satellite dish at sunset, and a laptop showing network cabling"></div>

  <div class="about-body">
    <p><strong>Lorem ipsum dolor sit amet,</strong> euismod faucibus lobortis in imperdiet, etiam eu diam, in pede nec. Rhoncus a cras venenatis. Cras ornare tincidunt convallis sem, et libero luctus in lacus pellentesque, eget malesuada ac, ut faucibus, ipsum at ac. Mauris maecenas, turpis phasellus perspiciatis, id donec elit erat ante eu erat, cum maecenas massa iaculis tincidunt, orci fermentum erat. Lacus integer ris s aliquet sem. Vel ultricies vestibulum, at pellentesque turpis tincidunt, libero massa, elit vivamus mauris ut nunc officia rutrum.</p>
    <div class="callout">
      <h3>Cras ornare tincidunt convallis sem et libero</h3>
      <p>Lorem ipsum dolor sit amet, euismod faucibus lobortis in imperdiet, etiam eu diam, in pede nec. Rhoncus a cras venenatis. Cras ornare tincidunt convallis sem, et libero luctus in lacus pellentesque, eget malesuada ac, ut faucibus, ipsum at ac. Mauris maecenas, turpis phasellus perspiciatis, id donec elit erat ante eu erat, cum maecenas massa iaculis tincidunt, orci fermentum erat. Lacus integer ris aliquet sem.</p>
    </div>
    <div class="callout">
      <h3>Vel ultricies vestibulum at pellentesque</h3>
      <p>Lorem ipsum dolor sit amet, euismod faucibus lobortis in imperdiet, etiam eu diam, in pede nec. Rhoncus a cras venenatis. Cras ornare tincidunt convallis sem, et libero luctus in lacus pellentesque, eget malesuada ac, ut faucibus, ipsum at ac. Mauris maecenas, turpis phasellus perspiciatis, id donec elit erat ante eu erat, cum maecenas massa iaculis tincidunt, orci fermentum erat. Lacus integer ris aliquet sem.</p>
    </div>
  </div>

  <div class="service-photo" role="img" aria-label="Black and white photo of a hand holding a smartphone"></div>
  <article class="service-card">
    <h2>Home Automation</h2>
    <span class="bar"></span>
    <p>Enim urna neque suspendisse integer nunc, ridiculus lorem dolor turpis risus eros, et nunc, pharetra sodales a augue dui. Tellus vestibulum libero. Sed libero et eros posuere pellentesque. Sit diam</p>
  </article>
</body>
</html>
```